Label design for loose leaf tea pouches and tins

Starting my loose leaf tea business and looking for product labels.
I already have logo designed and would love it to be worked into the label;
Label sizes and sample text is in the attachments;
Pouches and tins pictures are also in the attachments.

looking for the recommendation on what is the best color for the pouch.
Updates

Here is the link: https://sheets.plorvane.example/grid/d/7kTq2mWx9LpZ4vRn8cYb3HsJf6DaE1uQ0oGtXiKe/edit

Adding the pdf since plorvane links do not work here

Target Market(s)

Women and men, 35+, USA

Font styles to use
Serif

Requirements
Must have
• Front and back label

```html
<!DOCTYPE html>
<html lang="en">
<head>
<meta charset="utf-8">
<title>Still Hour — Loose Leaf Tea Labels</title>
<link rel="stylesheet" href="https://fonts.googleapis.com/css2?family=Big+Shoulders+Display:wght@700&family=Archivo:wght@400;600;700&family=Yellowtail&display=swap">
<style>
  :root {
    --bg: #e9e9e9;
    --label: #f7f7f7;
    --label-shade: #dedede;
    --ink: #1a1a1a;
    --brand: #5f5f5f;
    --muted: #3a3a3a;
    --frame: #111111;
  }
  * { box-sizing: border-box; margin: 0; padding: 0; }
  html, body { width: 1200px; height: 1200px; overflow: hidden; }
  body {
    background: var(--bg);
    font-family: "Archivo", sans-serif;
    color: var(--ink);
    position: relative;
  }
  .label {
    position: absolute;
    top: 250px;
    width: 500px;
    height: 700px;
    background: linear-gradient(180deg, var(--label) 0%, var(--label) 45%, var(--label-shade) 100%);
    padding: 14px;
    box-shadow: 0 2px 8px rgba(0,0,0,.12);
  }
  .label--front { left: 60px; }
  .label--back { left: 640px; }
  .frame-outer {
    width: 100%; height: 100%;
    border: 5px solid var(--frame);
    padding: 5px;
  }
  .frame-inner {
    width: 100%; height: 100%;
    border: 2px solid var(--frame);
    position: relative;
    text-align: center;
  }
  .brand-mark {
    display: block;
    width: 78px; height: 78px;
    border-radius: 50%;
    background: var(--brand);
    margin: 0 auto;
  }
  .brand-name {
    font-family: "Big Shoulders Display", sans-serif;
    font-weight: 700;
    color: var(--brand);
    letter-spacing: 5px;
    font-size: 42px;
  }
  .script {
    font-family: "Yellowtail", cursive;
    color: var(--ink);
  }
  /* front */
  .label--front .brand-mark { margin-top: 70px; }
  .label--front .brand-name { margin-top: 28px; }
  .front-purity { margin-top: 100px; font-size: 14px; letter-spacing: 2px; color: var(--muted); }
  .front-title { font-size: 64px; margin-top: 18px; line-height: 1; }
  .front-tagline { margin-top: 30px; font-size: 12px; letter-spacing: 1.6px; line-height: 1.5; text-transform: uppercase; color: var(--muted); }
  .front-tagline strong { color: var(--ink); font-weight: 700; }
  .dots { margin-top: 8px; font-weight: 700; letter-spacing: 3px; font-size: 14px; }
  .front-type { margin-top: 6px; font-size: 21px; letter-spacing: 3px; }
  .front-weight { margin-top: 8px; font-size: 15px; }
  /* back */
  .back-head { display: flex; justify-content: space-between; align-items: flex-start; padding: 50px 30px 0 50px; }
  .back-product { text-align: center; }
  .back-product .script { font-size: 34px; color: #555; }
  .back-product .type { font-size: 19px; letter-spacing: 3px; color: #555; line-height: 1.3; margin-top: 6px; }
  .back-brand { text-align: center; }
  .back-brand .brand-mark { width: 58px; height: 58px; }
  .back-brand .brand-name { font-size: 30px; margin-top: 14px; letter-spacing: 4px; }
  .section-title { font-weight: 700; letter-spacing: 2px; font-size: 14px; margin-bottom: 4px; }
  .section-body { font-size: 14px; line-height: 1.45; padding: 0 18px; }
  .benefits { margin-top: 48px; }
  .ingredients { margin-top: 36px; }
  .back-foot { display: flex; justify-content: space-around; margin-top: 28px; font-size: 13.5px; line-height: 1.55; }
  .back-foot .origin { margin-top: 22px; }
  .back-foot .pack .type { letter-spacing: 2px; font-size: 15px; }
  .back-foot strong { letter-spacing: 1.5px; font-weight: 700; }
</style>
</head>
<body>
  <section class="label label--front">
    <div class="frame-outer">
      <div class="frame-inner">
        <span class="brand-mark" aria-hidden="true"></span>
        <div class="brand-name">LEAF &amp; KETTLE</div>
        <p class="front-purity">100 % PUR ORGANIC</p>
        <h1 class="front-title script">Still Hour</h1>
        <p class="front-tagline">Delicious concoction of Indian herbs<br>and flowers to help you<br><strong>Settle in and unwind</strong></p>
        <div class="dots">■■■</div>
        <p class="front-type">LOOSE LEAF TEA</p>
        <p class="front-weight">NET.WT. 3.4 OZ / 100g</p>
      </div>
    </div>
  </section>

  <section class="label label--back">
    <div class="frame-outer">
      <div class="frame-inner">
        <div class="back-head">
          <div class="back-product">
            <div class="script">Still Hour</div>
            <div class="type">LOOSE LEAF<br>TEA</div>
          </div>
          <div class="back-brand">
            <span class="brand-mark" aria-hidden="true"></span>
            <div class="brand-name">LEAF &amp; KETTLE</div>
          </div>
        </div>
        <div class="benefits">
          <p class="section-title">BENEFITS:</p>
          <p class="section-body">Truly magic wellness potion formulated with combination of world-class ingridients. Still Hour tea calms you down, warms you up, eases anxiety and fights signs of depression. Turmeric, cardamom and ginger reduce symptoms of gas and bloating and facilitate digestion.</p>
        </div>
        <div class="ingredients">
          <p class="section-title">INGRIDIENTS:</p>
          <p class="section-body">Chamomile, Mary Gold, Rooibos, Liquorice Root, Apple, Lemon Peels, Cloves, Black Cardamom, Turmeric, Ginger</p>
        </div>
        <div class="back-foot">
          <p class="origin">Country of origin:<br>India<br>Loose Leaf Tea</p>
          <p class="pack"><span class="type">LOOSE LEAF TEA</span><br>50 servings<br><strong>DECAFFINATED</strong></p>
        </div>
      </div>
    </div>
  </section>
</body>
</html>
```